Oral Surgeon Referral Pads

Hello. We need referral pads for Dr Loretta Pembrooke, DDS board certified oral surgeon's new office - Cedar Hollow Oral & Maxillofacial Surgery. See logo uploaded. See some images we would like included
Updates

Designs look the same

Font styles to use
Serif
Script

Colors
00AB8E
00BBA5
67D7C9
C6EFE9
E9F9F6

Requirements
Must have
• Color Pantone 623c. Also foldable business cards

```html
<!DOCTYPE html>
<html lang="en">
<head>
<meta charset="utf-8">
<title>Cedar Hollow Oral &amp; Maxillofacial Surgery – Referral Stationery</title>
<link href="https://fonts.googleapis.com/css2?family=Tinos:wght@400;700&family=Questrial&family=Open+Sans:wght@400;600&display=swap" rel="stylesheet">
<style>
  :root {
    --brand: #00ab8e;
    --brand-mid: #00bba5;
    --brand-soft: #67d7c9;
    --brand-pale: #c6efe9;
    --brand-mist: #e9f9f6;
    --paper: #ffffff;
    --backdrop: #e6e8ea;
    --ink-grey: #6f6f6f;
    --body-grey: #8c8c8c;
    --dark-text: #444444;
  }
  * { margin: 0; padding: 0; box-sizing: border-box; }
  html, body { width: 1200px; height: 960px; overflow: hidden; }
  body { background: var(--backdrop); position: relative; font-family: "Tinos", serif; }

  .sheet { position: absolute; background: var(--paper); box-shadow: 0 4px 10px rgba(0,0,0,.16); overflow: hidden; }

  /* Business card – front */
  .card-front { left: 88px; top: 238px; width: 363px; height: 218px; }
  .card-front .holder-name { position: absolute; left: 25px; top: 24px; font: 700 15px "Tinos", serif; letter-spacing: .6px; color: var(--brand); white-space: nowrap; }
  .card-front .holder-title { position: absolute; left: 25px; top: 44px; font: 400 9.5px "Tinos", serif; color: var(--ink-grey); letter-spacing: .3px; }
  .card-front .title-rule { position: absolute; left: 25px; top: 60px; width: 33px; height: 1px; background: var(--ink-grey); }
  .contact-list { position: absolute; list-style: none; }
  .contact-list li { display: flex; align-items: flex-start; font: 400 8.4px/1.3 "Tinos", serif; color: var(--ink-grey); letter-spacing: .2px; white-space: nowrap; }
  .contact-list .icon { width: 11px; height: 11px; flex: none; margin-right: 4px; }
  .card-front .contact-list { left: 25px; top: 111px; }
  .card-front .contact-list li { margin-bottom: 6px; }
  .card-front .contact-list li.address { margin-bottom: 10px; }
  .footer-band { position: absolute; left: 0; bottom: 0; }

  /* Business card – back */
  .card-back { left: 88px; top: 504px; width: 363px; height: 218px; background: var(--brand); }
  .card-back .wordmark { position: absolute; left: 0; right: 0; top: 106px; text-align: center; color: #ffffff; }
  .wordmark-name { font: 400 21px/1 "Tinos", serif; letter-spacing: .8px; }
  .wordmark-sub { font: 400 10.5px/1 "Tinos", serif; letter-spacing: .3px; margin-top: 6px; }
  .card-back .logo-dot { position: absolute; left: 174px; top: 64px; width: 16px; height: 16px; border: 1.5px solid #ffffff; border-radius: 50%; }

  /* Letterhead */
  .letterhead { left: 530px; top: 72px; width: 583px; height: 817px; }
  .letterhead .wordmark { position: absolute; left: 20px; width: 186px; top: 76px; text-align: center; color: var(--brand); }
  .letterhead .logo-dot { position: absolute; left: 105px; top: 36px; width: 17px; height: 17px; border: 1.5px solid var(--brand); border-radius: 50%; }
  .letterhead .contact-list { left: 418px; top: 40px; }
  .letterhead .contact-list li { margin-bottom: 7px; }
  .letterhead .contact-list li.address { margin-bottom: 10px; }

  .recipient { position: absolute; left: 38px; top: 178px; }
  .recipient-name { font: 700 17px "Tinos", serif; color: var(--dark-text); letter-spacing: .3px; margin-bottom: 6px; }
  .recipient-line { font: 400 10.5px/1.4 "Open Sans", sans-serif; color: var(--body-grey); }
  .recipient-line + .recipient-line { margin-top: 4px; }
  .recipient-line.tight { margin-top: 0; }
  .letter-date { position: absolute; right: 43px; top: 261px; font: 600 12px "Open Sans", sans-serif; color: #8a8a8a; }

  .letter-body { position: absolute; left: 38px; top: 294px; width: 502px; }
  .letter-body p { font: 400 13px/18px "Questrial", sans-serif; color: var(--body-grey); text-align: justify; margin-bottom: 18px; }

  .signatory { position: absolute; left: 46px; top: 605px; font: 700 13px "Tinos", serif; color: var(--dark-text); }
  .signature-area { position: absolute; left: 66px; top: 634px; width: 92px; height: 56px; background: var(--brand-mist); border-radius: 4px; }
</style>
</head>
<body>

<svg width="0" height="0" style="position:absolute">
  <defs>
    <symbol id="icon-pin" viewBox="0 0 12 12"><rect width="12" height="12" rx="1.5" fill="#00ab8e"/><path d="M6 2.2a2.6 2.6 0 0 0-2.6 2.6C3.4 6.8 6 9.8 6 9.8s2.6-3 2.6-5A2.6 2.6 0 0 0 6 2.2z" fill="#fff"/><circle cx="6" cy="4.8" r="1" fill="#00ab8e"/></symbol>
    <symbol id="icon-phone" viewBox="0 0 12 12"><rect width="12" height="12" rx="1.5" fill="#00ab8e"/><path d="M3.6 2.6l1.3 0 .6 1.9-.9.7a5 5 0 0 0 2.2 2.2l.7-.9 1.9.6v1.3c0 .4-.3.7-.7.7A6.4 6.4 0 0 1 2.9 3.3c0-.4.3-.7.7-.7z" fill="#fff"/></symbol>
    <symbol id="icon-mail" viewBox="0 0 12 12"><rect width="12" height="12" rx="1.5" fill="#00ab8e"/><rect x="2.3" y="3.4" width="7.4" height="5.2" fill="none" stroke="#fff" stroke-width=".9"/><path d="M2.3 3.4L6 6.4l3.7-3" fill="none" stroke="#fff" stroke-width=".9"/></symbol>
    <symbol id="icon-cursor" viewBox="0 0 12 12"><rect width="12" height="12" rx="1.5" fill="#00ab8e"/><path d="M4 2.4v6.8l1.6-1.5 1.1 2.3 1-.5-1.1-2.2 2.1-.1z" fill="#fff"/></symbol>
  </defs>
</svg>

<!-- Business card front -->
<section class="sheet card-front">
  <h2 class="holder-name">Dr Loretta Pembrooke</h2>
  <p class="holder-title">Oral Surgeon, DDS</p>
  <div class="title-rule"></div>
  <ul class="contact-list">
    <li class="address"><svg class="icon"><use href="#icon-pin"/></svg><span>712 Larkspur Avenue<br>Fairmont, OR 97310</span></li>
    <li><svg class="icon"><use href="#icon-phone"/></svg><span>+00 555 204 61</span></li>
    <li><svg class="icon"><use href="#icon-mail"/></svg><span>office@cedarhollowsurgery.com</span></li>
    <li><svg class="icon"><use href="#icon-cursor"/></svg><span>www.cedarhollowsurgery.com</span></li>
  </ul>
  <svg class="footer-band" width="363" height="12" viewBox="0 0 363 12"><polygon points="0,0 217,0 226,12 0,12" fill="#00ab8e"/></svg>
</section>

<!-- Business card back -->
<section class="sheet card-back">
  <div class="logo-dot"></div>
  <div class="wordmark">
    <div class="wordmark-name">Cedar Hollow</div>
    <div class="wordmark-sub">Oral &amp; Maxillofacial Surgery</div>
  </div>
</section>

<!-- Referral letterhead -->
<section class="sheet letterhead">
  <div class="logo-dot"></div>
  <div class="wordmark">
    <div class="wordmark-name">Cedar Hollow</div>
    <div class="wordmark-sub">Oral &amp; Maxillofacial Surgery</div>
  </div>

  <ul class="contact-list">
    <li class="address"><svg class="icon"><use href="#icon-pin"/></svg><span>712 Larkspur Avenue<br>Fairmont, OR 97310</span></li>
    <li><svg class="icon"><use href="#icon-phone"/></svg><span>+00 555 204 61</span></li>
    <li><svg class="icon"><use href="#icon-mail"/></svg><span>office@cedarhollowsurgery.com</span></li>
    <li><svg class="icon"><use href="#icon-cursor"/></svg><span>www.cedarhollowsurgery.com</span></li>
  </ul>

  <div class="recipient">
    <h3 class="recipient-name">Nora Whitfield</h3>
    <p class="recipient-line">0555-204-618</p>
    <p class="recipient-line">nora@whitfieldmail.com</p>
    <p class="recipient-line">88 Quarry Ln. Suite</p>
    <p class="recipient-line tight">40 Hartwell, GA 30643</p>
  </div>
  <p class="letter-date">12 December, 2024</p>

  <div class="letter-body">
    <p>Lorem ipsum dolor sit amet, consectetuer adipiscing elit, sed diam nonummy nibh euismod tincidunt ut laoreet dolore magna aliquam erat volutpat. Ut wisi enim ad minim veniam, quis nostrud exerci tation ullamcorper suscipit lobortis nisl ut aliquip ex ea commodo consequat. Duis autem vel eum iriure dolor in hendrerit in vulputate velit esse molestie consequat, vel illum dolore eu feugiat nulla facilisis at vero eros et accumsan et iusto odio dignissim qui blandit praesent luptatum zzril delenit augue duis dolore te feugait nulla facilisi.</p>
    <p>Lorem ipsum dolor sit amet, cons ectetuer adipiscing elit, sed diam nonummy nibh euismod tincidunt ut laoreet dolore magna aliquam erat volutpat. Ut wisi enim ad minim veniam, quis nostrud exerci tation ullamcorper suscipit lobortis nisl ut aliquip ex ea commodo consequat.</p>
    <p>Lorem ipsum dolor sit amet, consectetuer adipiscing elit, sed diam nonummy nibh euismod tincidunt ut laoreet dolore magna aliquam erat</p>
  </div>

  <p class="signatory">Dr Loretta Pembrooke</p>
  <div class="signature-area" role="img" aria-label="Handwritten signature of Dr Loretta Pembrooke"></div>

  <svg class="footer-band" width="583" height="13" viewBox="0 0 583 13"><polygon points="0,0 434,0 443,13 0,13" fill="#00ab8e"/></svg>
</section>

</body>
</html>
```